B2B Website for manufacturer of aerospace coatings

B2B Website for manufacturer of aerospace optical coatings and screens used in flight simulators and air-traffic controller centers. We sell to both the military as well as commercial airlines.

Colors: primary colors should be white and blue (same blue as in the logo), but you can accent with red, orange, or any other colors.

Main menu: Products, Services, About Us, Contact Us

Logo = See "Halden SkyLumen" JPEG attached.

We'd like a professional website that appeals to engineers at companies like Varnett, QORV, the military, etc.

We intend to build this website on WordPress.

Websites we like in our industry:
https://www.plexomirra.com/
https://www.dwo.com/civil-aviation/aviation-simulation-equipment/training-equipment/full-flight-simulators/
https://z7services.com/
https://www.lumbrexno.com/
https://kelvarnpq.com/
https://glimmerbayworks.com/

3 Pages: Homepage, Product page, Contact Us page

Target Market(s)

Varnett, Prescott Vayle, Corvane

Industry/Entity Type

Aerospace

Number of Pages Required

3 page

Colors
0054AA
0677BA
7BADD7
CADEEF
E8F1F8
F0912C
F2A743
F7CA91
FBE8D2
FDF5EE
EB3D1F
EC4F4E
F09395
F8D3D4
FCEDEE

Requirements
Should not have
• Black background

```html
<!DOCTYPE html>
<html lang="en">
<head>
<meta charset="utf-8">
<title>Halden SkyLumen — Optical Coatings for Military &amp; Aerospace</title>
<link rel="stylesheet" href="https://fonts.googleapis.com/css2?family=Titillium+Web:wght@300;400;600&family=Archivo:wght@400;500&display=swap">
<style>
  :root{
    --blue:#0054AA;
    --blue-line:#0677BA;
    --pale:#E8F1F8;
    --orange:#F0912C;
    --ink:#1d1d1f;
    --white:#ffffff;
  }
  *{box-sizing:border-box;margin:0;padding:0}
  html,body{width:1200px;height:2378px;overflow:hidden}
  body{position:relative;background:var(--white);font-family:"Titillium Web",sans-serif;color:var(--ink);font-weight:300}
  .abs{position:absolute}
  .btn{position:absolute;display:flex;align-items:center;justify-content:center;background:var(--blue);color:var(--white);font-size:13px;font-weight:400;text-decoration:none}
  .eyebrow{position:absolute;color:var(--blue);font-size:16px;font-weight:400}

  /* header */
  .site-header{position:absolute;left:0;top:0;width:1200px;height:82px;background:var(--white)}
  .brand{position:absolute;left:94px;top:29px;display:flex;align-items:center;gap:8px;color:var(--blue);font-size:20px;font-weight:600}
  .brand-mark{width:10px;height:10px;background:var(--blue);border-radius:50%}
  .main-nav a,.header-tools span{position:absolute;top:37px;font-family:"Archivo",sans-serif;font-size:12.5px;color:#111;text-decoration:none}
  .header-tools .cta{font-weight:500;font-size:13px}

  /* hero */
  .hero{position:absolute;left:0;top:82px;width:1200px;height:572px}
  .hero-photo{position:absolute;inset:0;background:
    radial-gradient(ellipse at 62% 45%,rgba(214,140,60,.55),rgba(0,0,0,0) 38%),
    linear-gradient(180deg,#1a1f2c 0%,#2d4d7a 28%,#3f6699 38%,#2a2a30 55%,#17161a 100%)}
  .hero-title{position:absolute;left:97px;top:190px;width:600px;color:var(--white);font-size:55px;line-height:62px;font-weight:300;white-space:nowrap}
  .hero-card{position:absolute;left:731px;top:364px;width:469px;height:208px;background:var(--white)}
  .hero-card h2{position:absolute;left:55px;top:48px;font-size:30px;line-height:35px;font-weight:300}
  .hero-card .rule{position:absolute;left:187px;top:109px;width:62px;height:1px;background:var(--blue)}
  .hero-card p{position:absolute;left:55px;top:150px;font-size:20px}

  /* intro */
  .intro-text{position:absolute;font-size:20px;line-height:29px}

  /* products */
  .products-photo{position:absolute;left:0;top:988px;width:616px;height:390px;background:linear-gradient(135deg,#8a6a45 0%,#c9cdd2 25%,#e2e5ea 50%,#b9bcc1 80%,#5e5a55 100%)}
  .products-title{position:absolute;left:711px;top:1026px;font-size:29px;font-weight:300}
  .body-copy{position:absolute;font-size:14.5px;line-height:22.5px;font-weight:300}

  /* services */
  .services{position:absolute;left:0;top:1378px;width:1200px;height:498px;background:var(--pale)}
  .services-heading{position:absolute;left:94px;top:160px;width:440px;font-size:41px;line-height:48px;font-weight:300;white-space:nowrap}
  .service-thumb{position:absolute;left:567px;width:109px;height:134px}
  .service-num{position:absolute;left:704px;font-size:16px}
  .service-name{position:absolute;left:704px;font-size:28px;font-weight:300}

  /* call to action */
  .cta-band{position:absolute;left:0;top:1876px;width:1200px;height:189px;background:var(--orange)}
  .cta-band p{position:absolute;left:94px;top:70px;color:var(--white);font-size:34px;font-weight:300}

  /* footer */
  .site-footer{position:absolute;left:0;top:2065px;width:1200px;height:313px;background:var(--blue);color:var(--white)}
  .site-footer .line{position:absolute;font-size:13px;font-weight:400}
  .footer-nav a{position:absolute;left:533px;font-size:13px;color:var(--white);text-decoration:none;font-weight:400}
  .social span{position:absolute;top:95px;width:16px;height:16px;border-radius:50%;border:2px solid var(--white)}
  .footer-rule{position:absolute;left:121px;top:240px;width:940px;height:1px;background:rgba(255,255,255,.7)}
  .copyright{position:absolute;left:0;width:1200px;top:263px;text-align:center;font-size:11.5px;font-weight:400}
</style>
</head>
<body>

<header class="site-header">
  <div class="brand"><span class="brand-mark"></span>Halden SkyLumen</div>
  <nav class="main-nav">
    <a style="left:366px" href="#">PRODUCTS</a>
    <a style="left:479px" href="#">SERVICES</a>
    <a style="left:585px" href="#">ABOUT US</a>
    <a style="left:692px" href="#">CONTACT US</a>
  </nav>
  <div class="header-tools">
    <svg class="abs" style="left:876px;top:37px" width="15" height="15" viewBox="0 0 24 24" fill="none" stroke="#111" stroke-width="1.8"><path d="M5 3h4l2 5-3 2a12 12 0 0 0 6 6l2-3 5 2v4a2 2 0 0 1-2 2A18 18 0 0 1 3 5a2 2 0 0 1 2-2z"/></svg>
    <span style="left:903px">021 7310 264</span>
    <span class="cta" style="left:1013px">GET IN TOUCH</span>
  </div>
</header>

<section class="hero">
  <div class="hero-photo" role="img" aria-label="Flight simulator cockpit at night with lit instrument panels and a projected runway view"></div>
  <h1 class="hero-title">Manufactur Optical<br>Coatings for Military/<br>Aerospace Applications</h1>
  <a class="btn" style="left:106px;top:402px;width:142px;height:47px" href="#">Our Products</a>
  <div class="hero-card">
    <h2>Let’s work<br>together</h2>
    <span class="rule"></span>
    <p>Contact us</p>
  </div>
</section>

<section class="intro">
  <span class="eyebrow" style="left:94px;top:722px">Who we are</span>
  <p class="intro-text" style="left:97px;top:758px;width:380px">Since Halden Optics’s founding in 1947, Halden has always been considered an optical house first that also happens to manufacture the world’s largest “Seamless” front and back projection screens.</p>
  <span class="eyebrow" style="left:532px;top:729px">Our Mission</span>
  <p class="intro-text" style="left:532px;top:768px;width:340px">provide the highest image fidelity to every project we undertake</p>
  <a class="btn" style="left:965px;top:745px;width:142px;height:47px" href="#">Learn more about us</a>
</section>

<section class="products">
  <div class="products-photo" role="img" aria-label="Large curved white projection screen in a workshop with a worker on a lift"></div>
  <span class="eyebrow" style="left:711px;top:996px">Our Products</span>
  <h2 class="products-title">Innovative Display Products</h2>
  <p class="body-copy" style="left:712px;top:1084px;width:365px">Lorem ipsum dolor sit amet consectetur. Facilisis elit euismod fusce morbi velit nibh neque. Lorem in morbi enim consectetur hendrerit et mattis eget. Risus vehicula enim fermentum urna vitae proin. Amet sodales etiam consequat lectus. Enim sed pellentesque morbi eu amet.</p>
  <a class="btn" style="left:717px;top:1233px;width:131px;height:47px" href="#">Learn more</a>
</section>

<section class="services">
  <span class="eyebrow" style="left:98px;top:104px">Our Services</span>
  <h2 class="services-heading">Highly responsive<br>support across the<br>entire system lifecycle</h2>

  <div class="service-thumb" style="top:103px;background:linear-gradient(180deg,#6d8fb8 0%,#7a8a5e 40%,#2b2f28 100%)" role="img" aria-label="Crew members in uniform at a simulator display"></div>
  <span class="service-num" style="top:102px">01</span>
  <h3 class="service-name" style="top:128px">Mirror re-skins</h3>
  <p class="body-copy" style="left:704px;top:186px;width:350px">Lorem ipsum dolor sit amet consectetur. Facilisis elit euismod fusce morbi velit nibh neque.</p>

  <div class="service-thumb" style="top:270px;background:linear-gradient(160deg,#e9ecef 0%,#c8ccd2 55%,#4a4d52 100%)" role="img" aria-label="White full flight simulator cabin on motion platform"></div>
  <span class="service-num" style="top:268px">02</span>
  <h3 class="service-name" style="top:294px">Relocation</h3>
  <p class="body-copy" style="left:704px;top:345px;width:350px">Lorem ipsum dolor sit amet consectetur. Facilisis elit euismod fusce morbi velit nibh neque.</p>
</section>

<section class="cta-band">
  <p>See how our can help — contact us now.</p>
  <a class="btn" style="left:918px;top:69px;width:131px;height:47px" href="#">Learn more</a>
</section>

<footer class="site-footer">
  <span class="line" style="left:197px;top:92px">Your company address</span>
  <span class="line" style="left:200px;top:112px">02043</span>
  <svg class="abs" style="left:199px;top:145px" width="13" height="13" viewBox="0 0 24 24" fill="none" stroke="#fff" stroke-width="1.8"><path d="M5 3h4l2 5-3 2a12 12 0 0 0 6 6l2-3 5 2v4a2 2 0 0 1-2 2A18 18 0 0 1 3 5a2 2 0 0 1 2-2z"/></svg>
  <span class="line" style="left:220px;top:144px">021 7310 264</span>
  <svg class="abs" style="left:200px;top:175px" width="14" height="12" viewBox="0 0 24 20" fill="none" stroke="#fff" stroke-width="1.8"><rect x="1" y="1" width="22" height="18" rx="2"/><path d="M1 3l11 8 11-8"/></svg>
  <span class="line" style="left:224px;top:173px">info@haldenskylumen.com</span>

  <nav class="footer-nav">
    <a style="top:87px" href="#">Home</a>
    <a style="top:112px" href="#">Products</a>
    <a style="top:137px" href="#">Services</a>
    <a style="top:162px" href="#">About us</a>
    <a style="top:187px" href="#">Contact us</a>
  </nav>

  <div class="social" aria-label="Social links">
    <span style="left:924px"></span>
    <span style="left:974px"></span>
    <span style="left:1024px"></span>
  </div>

  <div class="footer-rule"></div>
  <p class="copyright">© 2022 Halden SkyLumen | All Rights Reserved</p>
</footer>

</body>
</html>
```